Square Business Cards for Our Restaurant / Event Venue

We need square business cards designed for the management team of our event venue and restaurant. On one side of the card should be the the Harbor Lantern 7 logo and URL www.harborlantern7.example. On the other side should be the Ember Logo and URL www.emberhall7.example. All employee details should be on the side with Ember logo. There will be a total of 5 cards to be created with the design.

Clara Bennquist
clara@harborlantern7.example

main 555.418.3072
direct 555.730.2946

4831 West Orchard Lane SE
Washington, DC 90417

Industry/Entity Type

Business

```html
<!DOCTYPE html>
<html lang="en">
<head>
<meta charset="utf-8">
<title>Ember &amp; Harbor Lantern 7 — Square Business Cards</title>
<link rel="stylesheet" href="https://fonts.googleapis.com/css2?family=Work+Sans:wght@400;500&family=Yellowtail&display=swap">
<style>
  :root {
    --page-bg: #ffffff;
    --card-white: #ffffff;
    --card-edge: #e6e6e6;
    --ink: #1d1d1d;
    --brand-red: #b8232a;
    --red-light: #c33e44;
    --red-deep: #b21f26;
    --text-white: #ffffff;
  }
  * { box-sizing: border-box; margin: 0; padding: 0; }
  html, body {
    width: 1200px;
    height: 840px;
    overflow: hidden;
    background: var(--page-bg);
  }
  .canvas {
    position: relative;
    width: 1200px;
    height: 840px;
    font-family: "Work Sans", Arial, sans-serif;
  }
  .card {
    position: absolute;
    top: 198px;
    width: 444px;
    height: 444px;
    border-radius: 22px;
    overflow: hidden;
  }
  /* Front: Ember + contact details */
  .card--front {
    left: 130px;
    background: var(--card-white);
    border: 1px solid var(--card-edge);
  }
  .front__brand {
    position: absolute;
    left: 30px;
    top: 72px;
    font-size: 58px;
    font-weight: 500;
    line-height: 1;
    color: var(--ink);
    letter-spacing: 0.5px;
  }
  .front__name {
    position: absolute;
    left: 30px;
    top: 224px;
    font-family: "Yellowtail", cursive;
    font-size: 34px;
    line-height: 1;
    color: var(--brand-red);
  }
  .front__rule {
    position: absolute;
    left: 31px;
    top: 276px;
    width: 20px;
    height: 1.5px;
    background: var(--brand-red);
  }
  .front__address {
    position: absolute;
    left: 30px;
    top: 290px;
    font-size: 15px;
    line-height: 20px;
    color: var(--ink);
    font-style: normal;
  }
  .front__contacts {
    position: absolute;
    left: 30px;
    top: 336px;
    list-style: none;
    font-size: 15px;
    line-height: 20px;
    color: var(--ink);
  }
  .contact-row {
    display: flex;
    align-items: center;
    gap: 7px;
  }
  .contact-row svg {
    width: 11px;
    height: 11px;
    flex: none;
  }
  .accent { color: var(--brand-red); }

  /* Back: Harbor Lantern 7 */
  .card--back {
    left: 628px;
    background: linear-gradient(160deg, var(--red-light) 0%, var(--red-deep) 60%, var(--red-deep) 100%);
  }
  .back__brand {
    position: absolute;
    left: 0;
    right: 0;
    top: 200px;
    display: flex;
    justify-content: center;
    align-items: center;
    gap: 12px;
    color: var(--text-white);
    font-size: 30px;
    font-weight: 500;
    line-height: 1;
  }
  .back__dot {
    width: 22px;
    height: 22px;
    border-radius: 50%;
    background: var(--text-white);
  }
  .back__url {
    position: absolute;
    left: 0;
    right: 0;
    top: 380px;
    text-align: center;
    color: var(--text-white);
    font-size: 15px;
    letter-spacing: 0.3px;
  }
</style>
</head>
<body>
<main class="canvas">

  <section class="card card--front" aria-label="Ember business card, front">
    <div class="front__brand">Ember</div>
    <h1 class="front__name">Clara Bennquist</h1>
    <div class="front__rule"></div>
    <address class="front__address">
      4831 West Orchard Lane SE<br>
      Washington, DC 90417
    </address>
    <ul class="front__contacts">
      <li class="contact-row">
        <svg viewBox="0 0 12 12" aria-label="main phone"><path d="M2.5 1 L4.5 1 L5 3.5 L3.8 4.4 Q4.8 6.8 7.6 8.2 L8.5 7 L11 7.5 L11 9.5 Q10.5 11 9 11 Q2 9.8 1 3 Q1 1.5 2.5 1 Z" fill="none" stroke="var(--brand-red)" stroke-width="1.2"/></svg>
        <span>555.418.3072</span>
      </li>
      <li class="contact-row">
        <svg viewBox="0 0 12 12" aria-label="direct phone"><rect x="3" y="1" width="6" height="10" rx="1" fill="none" stroke="var(--brand-red)" stroke-width="1.3"/><line x1="5" y1="9" x2="7" y2="9" stroke="var(--brand-red)" stroke-width="1"/></svg>
        <span>555.730.2946</span>
      </li>
      <li class="contact-row">
        <svg viewBox="0 0 12 12" aria-label="email"><rect x="1" y="2.5" width="10" height="7" fill="none" stroke="var(--brand-red)" stroke-width="1.2"/><path d="M1 2.5 L6 6.5 L11 2.5" fill="none" stroke="var(--brand-red)" stroke-width="1.2"/></svg>
        <span>clara@harborlantern7.example</span>
      </li>
      <li class="contact-row">
        <svg viewBox="0 0 12 12" aria-label="website"><circle cx="6" cy="6" r="5" fill="none" stroke="var(--brand-red)" stroke-width="1"/><ellipse cx="6" cy="6" rx="2.2" ry="5" fill="none" stroke="var(--brand-red)" stroke-width="0.9"/><line x1="1" y1="6" x2="11" y2="6" stroke="var(--brand-red)" stroke-width="0.9"/></svg>
        <span>www.<span class="accent">harborlantern7</span>.example</span>
      </li>
    </ul>
  </section>

  <section class="card card--back" aria-label="Harbor Lantern 7 business card, back">
    <div class="back__brand">
      <span class="back__dot"></span>
      <span>Harbor Lantern 7</span>
    </div>
    <div class="back__url">www.emberhall7.example</div>
  </section>

</main>
</body>
</html>
```